Website Design for a Project Management Consulting Business

I have a logo design already and now I need a website.
I am a project manager and run my own consulting business.
Currently I am under contract with 3 major Kestrelmark 300 companies. I'd like a website I can direct current and future clients.
My job is running IT projects and working with developers to deliver business priorities.
The website should be professional and clean - I work IT projects and would like to incorporate that into any theme.
I'd like the site to have several page or breakoff links - sections would include : about me, about my services, a page to display all of my certification badges, another page to talk about highlights from past projects and so on.
Looking for a collaborative experience.

Industry/Entity Type

Kestrelmark 300 Consulting Firm - Project Management

Coding

Coded - Design and coding required

Number of Pages Required

1 page

Font styles to use
Serif

Colors
0094D4
00A9DD
6FCCEA
C7EBF8
E9F6FB
EE7325
F08F49
F5BC92
FAE3D3
FDF4ED

Requirements
Must have
• Sections that are a must: About Me (bio), About My Services, About my Certifications and Credentials, Experience on Past Projects,
Nice to have
• I have added the logo below - I'd like to use the logo and have it prominent ; should be professional and inviting

```html
<!DOCTYPE html>
<html lang="en">
<head>
<meta charset="utf-8">
<title>Steadfast Project Partners</title>
<link href="https://fonts.googleapis.com/css2?family=Lexend:wght@300;400;500;600;700&family=Roboto:wght@300;400;500;700&display=swap" rel="stylesheet">
<style>
:root{
  --navy:#103a6b;
  --navy-deep:#0c3466;
  --orange:#ee7325;
  --orange-soft:#f08f49;
  --peach:#fdf2ea;
  --peach-2:#fae3d3;
  --text:#333a44;
  --muted:#6d737b;
  --white:#ffffff;
  --line:#e6e6e6;
}
*{box-sizing:border-box;margin:0;padding:0}
html,body{width:1200px;height:3531px;overflow:hidden}
body{position:relative;background:var(--white);font-family:'Roboto',sans-serif;color:var(--text)}
.abs{position:absolute}
.head{font-family:'Lexend',sans-serif}
a{color:inherit;text-decoration:none}

/* hero */
.hero{left:0;top:0;width:1200px;height:570px;background:linear-gradient(120deg,#0b3f6a 0%,#0f5d86 45%,#1a6f93 70%,#0e4b74 100%)}
.hero-shade{left:0;top:0;width:1200px;height:570px;background:radial-gradient(ellipse at 60% 20%,rgba(60,150,190,.45),transparent 60%)}
.nav{left:112px;top:36px;width:976px;height:68px;background:var(--white);border-radius:3px;box-shadow:0 4px 14px rgba(0,0,0,.12)}
.brand{left:24px;top:18px;display:flex;align-items:center;gap:8px;font-family:'Lexend',sans-serif;font-weight:600;font-size:17px;color:var(--navy);letter-spacing:.3px}
.brand i{display:block;width:24px;height:24px;border:2px solid var(--navy)}
.menu{left:265px;top:26px;display:flex;gap:26px;font-size:12.5px;color:#222}
.menu .on{color:var(--orange)}
.talk{left:866px;top:18px;width:84px;height:32px;background:var(--navy);color:#fff;border-radius:3px;font-size:12.5px;font-weight:500;display:flex;align-items:center;justify-content:center}
.hero-title{left:0;width:1200px;top:222px;text-align:center;font-family:'Lexend',sans-serif;font-weight:600;font-size:36px;color:#fff}
.hero-sub{left:0;width:1200px;top:282px;text-align:center;font-size:18px;line-height:27px;color:#e8f1f7;font-weight:300}
.hero-btn{left:522px;top:358px;width:154px;height:38px;border:2px solid #fff;color:#fff;font-weight:600;font-size:15px;display:flex;align-items:center;justify-content:center;gap:8px}

/* services */
.panel{left:112px;top:517px;width:976px;height:70px;background:#fff;border-radius:6px 6px 0 0}
.eyebrow{font-family:'Lexend',sans-serif;font-size:13px;color:#333}
.sec-title{font-family:'Lexend',sans-serif;font-weight:300;font-size:36px;color:var(--navy)}
.sec-title b{font-weight:600;color:var(--orange)}
.card{top:669px;width:268px;height:403px}
.card.lift{background:#fff;box-shadow:0 6px 28px rgba(0,0,0,.10);border-radius:4px}
.card .ic{position:absolute;left:26px;top:24px}
.card h3{position:absolute;left:26px;top:92px;font-family:'Lexend',sans-serif;font-weight:400;font-size:19px;color:#222}
.card.lift h3{color:var(--navy)}
.card p{position:absolute;left:26px;top:132px;width:222px;font-size:15px;line-height:26.5px;color:#555;font-weight:300}
.card.lift p{color:#333}
.card .more{position:absolute;left:26px;top:346px;font-size:12px;font-weight:700;color:var(--navy);text-decoration:underline}
.card.lift .more{color:var(--orange)}
.dots{left:112px;top:1161px;width:976px;border-top:2px dotted #bdbdbd}

/* about */
.stats{left:196px;top:1251px;width:390px;height:371px;border:1px solid var(--line)}
.cell{position:absolute;width:195px;height:155px;border-right:1px solid var(--line);border-bottom:1px solid var(--line);text-align:center}
.cell strong{display:block;margin-top:40px;font-family:'Lexend',sans-serif;font-weight:500;font-size:36px;color:var(--orange)}
.cell span{font-size:15px;color:#222}
.portrait{left:200px;top:1365px;width:180px;height:257px;background:linear-gradient(180deg,#7f9ab3 0%,#5f7ea0 60%,#455f7f 100%);border-radius:90px 90px 0 0}
.namebar{left:196px;top:1561px;width:390px;height:61px;background:var(--peach)}
.namebar h4{position:absolute;left:195px;top:8px;font-family:'Lexend',sans-serif;font-weight:500;font-size:19px;color:var(--navy)}
.namebar em{position:absolute;left:195px;top:35px;font-size:11px;color:#333}
.about-copy{left:669px;top:1322px;width:320px}
.about-copy .lead{font-size:16px;line-height:24.5px;color:#222}
.about-copy .body{margin-top:18px;font-size:13px;line-height:23px;color:#333;font-weight:300}
.btn-navy{background:var(--navy);color:#fff;font-size:13px;font-weight:600;display:flex;align-items:center;justify-content:center;gap:8px;border-radius:2px}

/* cases */
.cases{left:0;top:1712px;width:1200px;height:700px;background:var(--peach)}
.case-shot{left:112px;top:1898px;width:641px;height:425px;background:#fff}
.case-mock{left:290px;top:1950px;width:412px;height:318px;background:linear-gradient(135deg,#0e4d78,#1a6b93 60%,#e8eef3 62%,#fff);box-shadow:0 10px 24px rgba(0,0,0,.18)}
.case-over{left:112px;top:1898px;width:308px;height:425px;background:linear-gradient(180deg,rgba(240,143,73,.92),rgba(238,115,37,.95))}
.case-txt{color:#fff}
.small-case{left:779px;width:309px;height:200px;background:linear-gradient(160deg,#f5a56b,#ee7b33)}
.link-w{color:#fff;font-weight:600;font-size:13px;border-bottom:1px solid #fff;padding-bottom:2px}

/* certs */
.vdash{left:600px;top:2412px;height:548px;border-left:1px dashed #d0d0d0}
.cert{top:2606px;width:389px;height:352px;background:var(--peach)}
.cert-top{position:absolute;left:0;top:0;width:389px;height:146px;background:#fff;border-top:4px solid var(--navy);box-shadow:0 2px 10px rgba(0,0,0,.05)}
.cert-top h3{position:absolute;left:26px;top:22px;font-family:'Lexend',sans-serif;font-weight:500;font-size:20px;color:#222}
.cert-top p{position:absolute;left:26px;top:56px;width:345px;font-size:12.5px;line-height:21px;color:#333}
.badge{position:absolute;top:206px;width:120px;height:120px;border-radius:50%}
.doc{position:absolute;top:188px;width:148px;height:126px;background:#fff;border:1px solid #cfd8de;box-shadow:0 3px 8px rgba(0,0,0,.08)}
.arrow-c{position:absolute;width:28px;height:28px;border-radius:50%;border:1px solid #ddd;background:#fff}
.arrow-c.on{background:var(--orange);border-color:var(--orange)}
.btn-orange{left:506px;top:3021px;width:188px;height:33px;background:var(--orange);color:#fff;font-size:13px;font-weight:600;display:flex;align-items:center;justify-content:center;gap:8px}

/* footer */
.footer{left:0;top:3143px;width:1200px;height:388px;background:var(--navy-deep);color:#e3eaf3}
.fcol{position:absolute;top:64px}
.fcol h5{font-family:'Lexend',sans-serif;font-weight:500;font-size:18px;color:#fff}
.fcol h5:after{content:"";display:block;width:34px;height:2px;background:var(--orange);margin-top:6px}
.fcol p,.fcol li{font-size:13px;line-height:20px;color:#d9e2ee;list-style:none}
.fbtn{display:inline-flex;align-items:center;gap:6px;border:1px solid #fff;padding:4px 10px;font-size:12px;color:#fff}
.soc{display:inline-block;width:30px;height:30px;border-radius:50%;border:1px solid #9fb3cc;margin-right:8px}
.soc.on{background:var(--orange);border-color:var(--orange)}
.email{width:225px;height:26px;border:1px solid #fff;display:flex;align-items:center;gap:8px;padding-left:10px;font-size:11.5px;color:#c9d4e2}
.sub{display:inline-block;margin-top:10px;background:var(--orange);color:#fff;padding:5px 12px;font-size:12px;font-weight:600}
.fbar{left:112px;top:326px;width:976px;border-top:1px solid rgba(255,255,255,.18)}
.copy{left:112px;top:350px;font-size:12px;color:#b9c6d6}
.copy b{color:var(--orange);font-weight:600}
.fnav{right:112px;top:350px;font-size:12px;color:#d9e2ee}
</style>
</head>
<body>

<!-- HERO -->
<div class="abs hero" role="img" aria-label="Team of developers working together at laptops in an office, tinted blue"></div>
<div class="abs hero-shade"></div>
<nav class="abs nav">
  <div class="abs brand"><i></i>Steadfast Partners</div>
  <div class="abs menu"><span class="on">Home</span><span>Services ▾</span><span>About</span><span>Case Studies</span><span>Certificates</span><span>Contact</span></div>
  <a class="abs talk">Let's Talk</a>
</nav>
<h1 class="abs hero-title">We have the plan to manage your plan!</h1>
<p class="abs hero-sub">Steadfast Project Partners, LLC has engaged on a<br>contract basis with Kestrelmark 300....</p>
<a class="abs hero-btn">Read More
  <svg width="18" height="18" viewBox="0 0 18 18"><circle cx="9" cy="9" r="8" fill="none" stroke="#fff" stroke-width="1.5"/><path d="M7.5 5.5 11 9l-3.5 3.5" fill="none" stroke="#fff" stroke-width="1.5"/></svg></a>

<!-- SERVICES -->
<div class="abs panel"></div>
<div class="abs eyebrow" style="left:0;width:1200px;top:568px;text-align:center">— What We Do —</div>
<h2 class="abs sec-title" style="left:0;width:1200px;top:580px;text-align:center">Featured <b>Services</b></h2>

<div class="abs card lift" style="left:170px">
  <svg class="ic" width="54" height="54" viewBox="0 0 54 54"><rect x="10" y="10" width="34" height="34" transform="rotate(45 27 27)" fill="var(--navy)"/></svg>
  <h3>Unified Scrum Master</h3>
  <p>Charged with leading Unified agile scrum teams consisting of various Mainframe, Distributed, and UX/UI Developers, QA testers, and Product Owners.</p>
  <a class="more">Learn More</a>
</div>
<div class="abs card" style="left:465px">
  <svg class="ic" width="54" height="54" viewBox="0 0 54 54"><circle cx="27" cy="27" r="24" fill="#fff" stroke="#5b2a86" stroke-width="3"/></svg>
  <h3>Project Manager</h3>
  <p>Directing and collaborating with development teams and business stakeholders in a hybrid waterfall/agile model delivering global, client facing Nimbus cloud based application solutions.</p>
  <a class="more">Learn More</a>
</div>
<div class="abs card" style="left:761px">
  <svg class="ic" width="54" height="54" viewBox="0 0 54 54"><circle cx="27" cy="27" r="24" fill="#fff" stroke="#5b2a86" stroke-width="3"/></svg>
  <h3>Program Manager</h3>
  <p>Brought in to apply traditional Waterfall PM organization and issue tracking methodologies to a global Cloudvane CRM rollout.</p>
  <a class="more">Learn More</a>
</div>
<div class="abs dots"></div>

<!-- ABOUT -->
<div class="abs stats">
  <div class="cell" style="left:0;top:0"><strong>500</strong><span>Contracted companies</span></div>
  <div class="cell" style="left:195px;top:0;border-right:none"><strong>12</strong><span>Years of experience</span></div>
  <div class="cell" style="left:195px;top:155px;border-right:none"><strong>3</strong><span>Project frameworks</span></div>
</div>
<div class="abs namebar"><h4>Marcus Delane</h4><em>Founder, Steadfast Project Partners, LLC</em></div>
<div class="abs portrait" role="img" aria-label="Portrait of the founder in a blue check suit"></div>
<div class="abs eyebrow" style="left:669px;top:1247px">— Who We Are</div>
<h2 class="abs sec-title" style="left:669px;top:1257px;text-align:left">About <b>Us</b></h2>
<div class="abs about-copy">
  <p class="lead">Marcus Delane is the Owner of Steadfast Project Partners, LLC and serves as Principal Lead Consultant on waterfall and agile contract opportunities.</p>
  <p class="body">Steadfast Project Partners, LLC has engaged on a contract basis with Kestrelmark 300 companies across various industries including banking and credit unions, global supply chain, and international food distribution. Marcus Delane brings 12 years of ...</p>
</div>
<a class="abs btn-navy" style="left:669px;top:1589px;width:121px;height:33px">Read More
  <svg width="14" height="14" viewBox="0 0 14 14"><circle cx="7" cy="7" r="7" fill="#fff"/><path d="M6 4l3 3-3 3" fill="none" stroke="var(--navy)" stroke-width="1.6"/></svg></a>

<!-- CASE STUDIES -->
<div class="abs cases"></div>
<div class="abs eyebrow" style="left:112px;top:1796px">— View Our Projects</div>
<h2 class="abs sec-title" style="left:112px;top:1808px">Case <b>Studies</b></h2>
<a class="abs" style="left:1006px;top:1818px;font-size:13px;font-weight:600;color:#222">View More →</a>

<div class="abs case-shot"></div>
<div class="abs case-mock" role="img" aria-label="Screenshot of a consulting website homepage"></div>
<div class="abs case-over"></div>
<div class="abs case-txt" style="left:147px;top:2138px;width:250px">
  <div style="font-weight:600;font-size:15px">1. —</div>
  <div class="head" style="font-weight:500;font-size:17px;line-height:23px;margin-top:4px">Lorem ipsum dolor sit amet, consectetur adip</div>
  <p style="font-size:12px;line-height:19px;margin-top:10px">Lorem ipsum dolor sit amet, consectetur adipiscing elit, sed do eiusmod</p>
  <a class="link-w" style="display:inline-block;margin-top:14px">View Project →</a>
</div>

<div class="abs small-case" style="top:1898px" role="img" aria-label="Project screenshot with orange overlay"></div>
<div class="abs case-txt" style="left:806px;top:1970px;width:270px">
  <div style="font-weight:600;font-size:14px">2.</div>
  <div class="head" style="font-weight:500;font-size:16px;line-height:22px">Lorem ipsum dolor sit amet, con sectetur adipis</div>
  <a class="link-w" style="display:inline-block;margin-top:12px">View Project →</a>
</div>
<div class="abs small-case" style="top:2123px;background:linear-gradient(160deg,#f7b98a,#f29a5b)" role="img" aria-label="Project screenshot of an about section"></div>

<!-- CERTIFICATION -->
<div class="abs vdash"></div>
<div class="abs eyebrow" style="left:0;width:1200px;top:2497px;text-align:center">— See Certifications and Credentials —</div>
<h2 class="abs sec-title" style="left:0;width:1200px;top:2510px;text-align:center">Our <b>Certification</b></h2>

<div class="abs cert" style="left:128px">
  <div class="cert-top"><h3>Certified Badges</h3><p>Lorem ipsum dolor sit amet, consectetur adipiscing elit, sed do eiusmod tempor incididunt ut labore et dolore magna aliqua. Quis ipsum</p></div>
  <div class="badge" style="left:48px;background:#f6b72a;border:5px solid #fbd36a"></div>
  <div class="badge" style="left:208px;background:#ec6a2c;border:5px solid #f59a6a"></div>
</div>
<div class="abs arrow-c" style="left:112px;top:2844px"></div>
<div class="abs arrow-c on" style="left:503px;top:2844px"></div>

<div class="abs cert" style="left:683px">
  <div class="cert-top"><h3>Certificates</h3><p>Lorem ipsum dolor sit amet, consectetur adipiscing elit, sed do eiusmod tempor incididunt ut labore et dolore magna aliqua. Quis ipsum</p></div>
  <div class="doc" style="left:37px" role="img" aria-label="Framed certificate of completion"></div>
  <div class="doc" style="left:206px" role="img" aria-label="Framed certificate of completion"></div>
</div>
<div class="abs arrow-c" style="left:667px;top:2844px"></div>
<div class="abs arrow-c" style="left:1058px;top:2844px"></div>

<a class="abs btn-orange">View All Certifications
  <svg width="14" height="14" viewBox="0 0 14 14"><circle cx="7" cy="7" r="7" fill="#fff"/><path d="M6 4l3 3-3 3" fill="none" stroke="var(--orange)" stroke-width="1.6"/></svg></a>

<!-- FOOTER -->
<footer class="abs footer">
  <div class="fcol" style="left:112px">
    <h5>Certification</h5>
    <div class="head" style="margin-top:26px;display:flex;align-items:center;gap:8px;font-weight:600;font-size:17px;color:#fff"><i style="display:block;width:28px;height:28px;border:2px solid #fff"></i>Steadfast Partners</div>
    <div style="margin-top:24px;display:flex;gap:12px">
      <span style="width:48px;height:48px;border-radius:50%;background:#f6b72a"></span>
      <span style="width:48px;height:48px;border-radius:50%;background:#ec6a2c"></span>
      <span style="width:48px;height:48px;border-radius:50%;background:#f6b72a"></span>
    </div>
  </div>
  <div class="fcol" style="left:362px;width:220px">
    <h5>Address</h5>
    <div style="margin-top:22px;display:flex;gap:12px">
      <svg width="12" height="16" viewBox="0 0 12 16" style="flex:none;margin-top:3px"><path d="M6 0a6 6 0 0 1 6 6c0 4-6 10-6 10S0 10 0 6a6 6 0 0 1 6-6z" fill="#fff"/><circle cx="6" cy="6" r="2.2" fill="var(--navy-deep)"/></svg>
      <p>Lorem ipsum Dolor, 4th Magna, Consectetur Adipiscing, UT ENIM, 012345</p>
    </div>
    <div style="margin-top:12px;display:flex;gap:12px">
      <svg width="14" height="14" viewBox="0 0 14 14" style="flex:none;margin-top:3px"><path d="M3 0l3 3-2 2c1 2 3 4 5 5l2-2 3 3-2 3C6 14 0 8 0 2z" fill="#fff"/></svg>
      <p style="line-height:15px">+1(123)-456-7890<br>+1(123)-456-7890</p>
    </div>
    <div style="margin-top:12px;display:flex;gap:12px;align-items:center">
      <svg width="15" height="11" viewBox="0 0 15 11"><rect width="15" height="11" fill="#fff"/><path d="M0 0l7.5 6L15 0" fill="none" stroke="var(--navy-deep)" stroke-width="1.4"/></svg>
      <p>hello@steadfastpp.com</p>
    </div>
  </div>
  <div class="fcol" style="left:612px;width:230px">
    <h5>Let's talk</h5>
    <p style="margin-top:22px">Your problem, our aim. Call us now for instant customer service.</p>
    <span class="fbtn" style="margin-top:12px">Get Started ⓘ</span>
    <div style="margin-top:22px"><span class="soc on"></span><span class="soc"></span><span class="soc"></span><span class="soc"></span><span class="soc"></span></div>
  </div>
  <div class="fcol" style="left:862px;width:226px">
    <h5>Subscribe Us</h5>
    <p style="margin-top:22px">Subscribe to our Newsletter for latest packages and offers.</p>
    <div class="email" style="margin-top:14px">
      <svg width="13" height="10" viewBox="0 0 13 10"><rect width="13" height="10" fill="#fff"/><path d="M0 0l6.5 5L13 0" fill="none" stroke="var(--navy-deep)" stroke-width="1.3"/></svg>Enter your email</div>
    <span class="sub">Subscribe</span>
  </div>
  <div class="abs fbar"></div>
  <div class="abs copy">© 2022 <b>Steadfast Project Partners, LLC</b> | All rights reserved</div>
  <div class="abs fnav">Home | Services | About Us | Certifications | Case Studies | Contact</div>
</footer>

</body>
</html>
```